Design eines Honigglases gesucht
Zielgruppe
Herstellung von exklusivem Honig. Es handelt sich um sehr hochwertigen Sidr Honig aus dem Yemen.
Aufgabenstellung
Es soll ein Honigglas entworfen werden. Das Honigglas soll sehr hochwertig und exklusiv wirken.

```html
<!DOCTYPE html>
<html lang="en">
<head>
<meta charset="utf-8">
<title>QAMRA Premium Honey – Jar Label</title>
<link rel="stylesheet" href="https://fonts.googleapis.com/css2?family=Josefin+Sans:wght@300;400&display=swap">
<style>
  :root {
    --page-bg: #e6e6e7;
    --label-black: #050505;
    --ornament-grey: #2e2e2e;
    --frame-line: #cfcfcf;
    --gold: #c9962e;
    --gold-soft: #d9ab45;
    --weight-text: #c8c8c8;
  }
  html, body {
    margin: 0;
    padding: 0;
    width: 1200px;
    height: 1200px;
    overflow: hidden;
    background: var(--page-bg);
  }
  .canvas {
    position: relative;
    width: 1200px;
    height: 1200px;
    display: flex;
    align-items: center;
    justify-content: center;
  }
  .jar-label {
    position: relative;
    width: 1100px;
    height: 720px;
    background: var(--label-black);
    overflow: hidden;
  }
  .ornament-band {
    position: absolute;
    left: 0;
    width: 100%;
    background: linear-gradient(90deg, var(--ornament-grey), #3a3a3a 50%, var(--ornament-grey));
  }
  .ornament-band--top { top: 0; height: 110px; }
  .ornament-band--bottom { bottom: 40px; height: 120px; }
  .brand-frame {
    position: absolute;
    left: 50%;
    top: 70px;
    transform: translateX(-50%);
    width: 430px;
    height: 430px;
    box-sizing: border-box;
    border: 2px solid var(--frame-line);
    background: var(--label-black);
    display: flex;
    flex-direction: column;
    align-items: center;
    justify-content: flex-start;
    padding-top: 58px;
  }
  .brand-square {
    width: 190px;
    height: 190px;
    background: linear-gradient(135deg, var(--gold-soft), var(--gold));
  }
  .brand-name {
    margin-top: 22px;
    font-family: "Josefin Sans", sans-serif;
    font-weight: 300;
    font-size: 84px;
    line-height: 1;
    letter-spacing: 2px;
    color: var(--gold);
  }
  .brand-tagline {
    margin-top: 12px;
    font-family: "Josefin Sans", sans-serif;
    font-weight: 300;
    font-size: 22px;
    letter-spacing: 5px;
    color: var(--gold);
  }
  .net-weight {
    position: absolute;
    left: 0;
    width: 100%;
    top: 570px;
    text-align: center;
    font-family: "Josefin Sans", sans-serif;
    font-weight: 300;
    font-size: 22px;
    color: var(--weight-text);
  }
</style>
</head>
<body>
  <main class="canvas">
    <section class="jar-label">
      <div class="ornament-band ornament-band--top" role="img" aria-label="Grey scroll and square ornament border"></div>
      <div class="ornament-band ornament-band--bottom" role="img" aria-label="Grey scroll and square ornament border"></div>
      <div class="brand-frame">
        <div class="brand-square"></div>
        <div class="brand-name">QAMRA</div>
        <div class="brand-tagline">PREMIUM HONEY</div>
      </div>
      <p class="net-weight">500 g</p>
    </section>
  </main>
</body>
</html>
```